Flyer für Anbieter von Gruppenritualen
Zielgruppe
Wir sind zwei Frauen (1x Yogalehrerin & Kalivento Therapeutin, 1x Ritualfachfrau), die regelmässig (aktuell 4x pro Jahr) Gruppenrituale anbieten. Unsere Zielgruppe sind vor allem Frauen (aber nicht ausschliesslich) jeglichen Alters, die sich etwas Schönes gönnen im Alltag.
Aufgabenstellung
Das Design soll ästhetisch schön und durchdacht sein. Ich schicke den Flyer mit, wie wir ihn bisher verwendet haben. Wir wünschen uns nun ein leichteres und stimmigeres Erscheinungsbild.
Praktisch wäre Format A5 oder 1:1.
Der Flyer soll die folgenden Elemente enthalten:
- Übersicht der 4 Daten + Veranstaltungsthemen
- Beschrieb, was eine Licht-Hain (so nennen sich unsere Gruppenrituale) ist
- ggf. Beschrieb vom Leitungsteam
Bei der Auswahl wird sicher auch eine Rolle spielen, ob das Design sich eignet zum Übertragen für die Ausschreibung der Einzelnenanlässe. Dazu schicke ich auch Beispiele, wie wir das letztes Jahr gemacht haben. Diese können auch als Inspiration für diesen Flyer dienen.
Konkrete Texte finden sich in einer Worddatei im Anhang zum Rauskopieren.

```html
<!DOCTYPE html>
<html lang="de">
<head>
<meta charset="utf-8">
<title>Licht-Hain Flyer</title>
<link rel="stylesheet" href="https://fonts.googleapis.com/css2?family=Limelight&family=Poppins:wght@400;700;800&display=swap">
<style>
:root{
  --page-bg:#e4e4e4;
  --paper:#ffffff;
  --ink:#111111;
  --gold:#c9a23d;
  --green:#2a9a4b;
  --blue:#2f5cab;
  --tone-green:#4aa365;
  --tone-blue:#4a6db5;
  --tone-yellow:#d4b04e;
  --tone-red:#d4494c;
  --panel:#eeeeef;
  --portrait:#b8b8b8;
  --divider:#d4d4d6;
}
*{box-sizing:border-box;margin:0;padding:0}
html,body{width:1062px;height:1200px;overflow:hidden;background:var(--page-bg)}
body{font-family:"Poppins",sans-serif;color:var(--ink);position:relative}
.flyer{position:absolute;left:141px;top:46px;width:780px;height:1107px;background:var(--paper);overflow:hidden}
.accent-bar{position:absolute;left:0;top:0;width:16px;height:279px;background:var(--gold)}
.title{position:absolute;left:60px;top:62px;font-family:"Limelight",serif;font-size:54px;font-weight:400;line-height:1;letter-spacing:-0.5px;white-space:nowrap}
.intro{position:absolute;left:63px;top:144px;width:312px;font-size:17.2px;line-height:23.4px}
.rule{position:absolute;left:63px;width:312px;height:2px}
.rule--gold{top:470px;background:var(--gold)}
.rule--green{top:741px;background:var(--green)}
.dates{position:absolute;left:63px;top:502px;width:340px;font-size:17.2px;line-height:23.4px}
.dates b,.info b{font-weight:700}
.info-heading{position:absolute;left:63px;top:768px;font-size:24px;font-weight:800;line-height:1.2}
.info{position:absolute;left:63px;top:814px;width:320px;font-size:17.2px;line-height:23.4px}
.nowrap{white-space:nowrap}
.color-photo{position:absolute;left:413px;top:0;width:367px;height:473px;background:linear-gradient(135deg,var(--tone-green) 0%,var(--tone-blue) 38%,var(--tone-yellow) 62%,var(--tone-red) 100%)}
.team{position:absolute;left:413px;top:493px;width:367px;height:594px;background:var(--panel);text-align:center}
.team-heading{position:absolute;left:0;right:0;top:15px;font-size:24px;font-weight:800;line-height:1.2}
.portrait{position:absolute;left:106px;width:155px;height:155px;border-radius:50%;background:var(--portrait)}
.portrait--first{top:61px}
.portrait--second{top:331px}
.member{position:absolute;left:0;right:0;font-size:15.3px;line-height:19.8px}
.member b{font-weight:700}
.member--first{top:229px}
.member--second{top:499px}
.team-divider{position:absolute;left:41px;width:276px;top:317px;height:2px;background:var(--divider)}
.bottom-band{position:absolute;left:0;bottom:0;width:780px;height:20px;background:var(--blue)}
</style>
</head>
<body>
<div class="flyer">
  <div class="accent-bar"></div>
  <h1 class="title">LICHT-Hain</h1>
  <p class="intro">In der Licht-Hain widmen wir uns einer Farbe und Themen, die mit dieser Farbe verknüpft sind. Genau wie die Oase in der Wüste ist die Licht-Hain ein Ort zum Auftanken, Entspannen und sich Nähren. In der Gruppetauchen wir tief ins Thema ein mit Achtsamkeitsübungen, Kalivento®, Bewegung, kreativen Momenten und Gruppenritualen.<br>Die Licht-Haine können einzeln oder als 4-teiligen Anlass besucht werden.</p>
  <div class="rule rule--gold"></div>
  <p class="dates">
    <b>ROT:</b> «Geerdet für sich einstehen»<br>
    Donnerstag, 20. März 2025<br>
    <b>BLAU:</b> «Sich nähren und in Fülle sein»<br>
    Dienstag, 17. Juni 2025<br>
    <b>GELB:</b> «Dankbar ernten»<br>
    Montag, 20. Oktober 2025<br>
    <b>GRÜN:</b> «Ausgeglichen auf dem Herzensweg»<br>
    Donnerstag, 4. Dezember 2024
  </p>
  <div class="rule rule--green"></div>
  <h2 class="info-heading">Mehr Informationen</h2>
  <p class="info">
    <b>Zeit:</b> 18:45-21:00 Uhr<br>
    <b>Ort:</b> Zwischenraum, Raum 113,<br>
    Lindenhofweg 12, 3008 Bern<br>
    <b>Anmeldung:</b> erfoderlich via<br>
    <span class="nowrap">regula-anderegg.ch</span> oder<br>
    <span class="nowrap">selina-vordemann.com</span><br>
    <b>Kosten:</b> CHF 50.-, reduziert, wenn mehrere Licht-Haine besucht werden. Solipreise möglich.
  </p>

  <div class="color-photo" role="img" aria-label="Foto von vier Farbflaschen in Grün, Blau, Gelb und Rot"></div>

  <section class="team">
    <h2 class="team-heading">Leitungsteam</h2>
    <div class="portrait portrait--first" role="img" aria-label="Porträtfoto von Selina Vordemann"></div>
    <p class="member member--first"><b>Selina Vordemann,</b><br>Kalivento® practitioner,<br>Yoga- und Achtsamkeitslehrerin<br>selina-vordemann.com</p>
    <div class="team-divider"></div>
    <div class="portrait portrait--second" role="img" aria-label="Porträtfoto von Regula Anderegg"></div>
    <p class="member member--second"><b>Regula Anderegg,</b><br>Fachfrau für Rituale und<br>Fotografin regula-anderegg.ch</p>
  </section>

  <div class="bottom-band"></div>
</div>
</body>
</html>
```